Business Card Design Project

Hi,
This is a simple contest. The logo for the back of the card is deigned. See attached files. The front of the card must have :

Directors Name: Dorian
Mob:
e-mail:
Postal Address:
Web Page Adress:

It may also add words: "Leaders in Construction Project Management Services"

Target Market(s)

Business & Home owners alike

Industry/Entity Type

Business

Requirements
Must have
• See details above and logo attached
Should not have
• Images other than logo

```html
<!DOCTYPE html>
<html lang="en">
<head>
<meta charset="utf-8">
<title>Meridian Works Australia – Business Card</title>
<link rel="stylesheet" href="https://fonts.googleapis.com/css2?family=Open+Sans:wght@400;700&family=Quicksand:wght@400;500&display=swap">
<style>
  :root {
    --brand-blue: #1a9ad6;
    --paper: #ffffff;
    --ink-grey: #7a7a7a;
    --divider: #9a9a9a;
    --backdrop: #e9e6e1;
  }
  * { box-sizing: border-box; margin: 0; padding: 0; }
  html, body {
    width: 1200px; height: 1000px; overflow: hidden;
    background: var(--backdrop);
  }
  .canvas { position: relative; width: 1200px; height: 1000px; }

  .card {
    position: absolute; width: 566px; overflow: hidden;
    box-shadow: 0 3px 10px rgba(0,0,0,.18);
  }
  .card--back { left: 70px; top: 42px; height: 308px; background: var(--brand-blue); z-index: 2; }
  .card--front { left: 580px; top: 287px; height: 311px; background: var(--paper); z-index: 1; }

  .wordmark {
    position: absolute; display: flex; align-items: center; gap: 12px;
    font-family: "Open Sans", sans-serif; font-weight: 700; white-space: nowrap;
  }
  .wordmark__square { width: 12px; height: 12px; flex: none; }
  .wordmark__text { line-height: 1; letter-spacing: 1px; }
  .card--back .wordmark { left: 0; right: 0; top: 142px; justify-content: center; color: var(--paper); }
  .card--back .wordmark__square { background: var(--paper); }
  .card--back .wordmark__text { font-size: 20px; }
  .card--front .wordmark { left: 74px; top: 70px; color: var(--brand-blue); }
  .card--front .wordmark__square { background: var(--brand-blue); width: 16px; height: 16px; }
  .card--front .wordmark__text { font-size: 25px; }

  .footer-band { position: absolute; left: 0; width: 566px; }
  .card--back .footer-band { top: 290px; height: 18px; }
  .card--front .footer-band { top: 290px; height: 21px; }
  .footer-band svg { position: absolute; inset: 0; }
  .tagline {
    position: absolute; left: 10px; top: 3px;
    font-family: "Open Sans", sans-serif; font-size: 11px; letter-spacing: .6px;
    color: var(--brand-blue); white-space: nowrap;
  }
  .band-name {
    position: absolute; right: 20px;
    font-family: "Open Sans", sans-serif; font-weight: 700; font-size: 11.5px; white-space: nowrap;
  }
  .card--back .band-name { color: var(--brand-blue); top: 2px; }
  .card--front .band-name { color: var(--paper); top: 5px; }

  .person { position: absolute; right: 310px; top: 186px; text-align: right; font-family: "Quicksand", sans-serif; }
  .person__name { font-size: 17px; color: var(--brand-blue); line-height: 1; }
  .person__role { font-size: 7px; letter-spacing: 2.4px; color: var(--brand-blue); margin-top: 1px; }
  .person__address { margin-top: 18px; font-size: 11.5px; line-height: 17px; color: var(--ink-grey); }

  .divider { position: absolute; left: 282px; top: 186px; width: 1px; height: 74px; background: var(--divider); }

  .contacts { position: absolute; left: 308px; top: 192px; list-style: none; font-family: "Quicksand", sans-serif; }
  .contacts li { display: flex; align-items: center; height: 20.5px; font-size: 11.5px; color: var(--ink-grey); white-space: nowrap; }
  .contacts svg { width: 14px; height: 14px; margin-right: 18px; fill: none; stroke: var(--brand-blue); stroke-width: 1.4; flex: none; }
</style>
</head>
<body>
<main class="canvas">

  <section class="card card--back" aria-label="Card back">
    <div class="wordmark">
      <span class="wordmark__square"></span>
      <span class="wordmark__text">MERIDIAN WORKS AUSTRALIA</span>
    </div>
    <div class="footer-band">
      <svg width="566" height="18" viewBox="0 0 566 18" aria-hidden="true">
        <rect width="566" height="18" fill="#ffffff"/>
        <polygon points="430,18 446,6 456,6 440,18" fill="#1a9ad6"/>
        <rect x="0" y="16" width="430" height="2" fill="#1a9ad6"/>
      </svg>
      <span class="tagline">LEADERS IN CONSTRUCTION PROJECT MANAGEMENT SERVICES</span>
      <span class="band-name">MERIDIAN</span>
    </div>
  </section>

  <section class="card card--front" aria-label="Card front">
    <div class="wordmark">
      <span class="wordmark__square"></span>
      <span class="wordmark__text">MERIDIAN WORKS AUSTRALIA</span>
    </div>

    <div class="person">
      <p class="person__name">Dorian</p>
      <p class="person__role">DIRECTOR</p>
      <p class="person__address">4120 Harbour Road Sydney,<br>NSW 2000</p>
    </div>

    <div class="divider"></div>

    <ul class="contacts">
      <li>
        <svg viewBox="0 0 14 14"><rect x="4" y="1" width="6" height="12" rx="1"/><line x1="6" y1="11" x2="8" y2="11"/></svg>
        555 234 017
      </li>
      <li>
        <svg viewBox="0 0 14 14"><rect x="1" y="3" width="12" height="8"/><polyline points="1,3 7,8 13,3"/></svg>
        hello@meridianworks.com
      </li>
      <li>
        <svg viewBox="0 0 14 14"><circle cx="7" cy="7" r="6"/><ellipse cx="7" cy="7" rx="2.6" ry="6"/><line x1="1" y1="7" x2="13" y2="7"/></svg>
        www.meridianworks.com
      </li>
    </ul>

    <div class="footer-band">
      <svg width="566" height="21" viewBox="0 0 566 21" aria-hidden="true">
        <rect x="0" y="0" width="566" height="1.5" fill="#1a9ad6"/>
        <rect x="0" y="5" width="566" height="16" fill="#1a9ad6"/>
        <polygon points="420,21 440,5 448,5 428,21" fill="#ffffff"/>
      </svg>
      <span class="band-name">MERIDIAN</span>
    </div>
  </section>

</main>
</body>
</html>
```